Business Card Design - Law Firm

We are a boutique law firm located near the beach in Manly, Australia. We have recently had a new logo designed and are revamping our business cards with the new logo.

We have recently had a business card design done for us but are not entirely happy with it. We are looking for something modern, simplistic but striking. We would like to see multiple designs.

We have attached a word document which includes our new logo and the current business card design which we are looking at moving away from.

We would like the business cards to be double sided. We would like the design to include something which we can print in gloss colour when we send it to the business card printers.

```html
<!DOCTYPE html>
<html lang="en">
<head>
<meta charset="utf-8">
<title>Harlow &amp; Partners Lawyers – Business Card</title>
<link href="https://fonts.googleapis.com/css2?family=Montserrat:wght@300;700&family=Lato:wght@400;700&display=swap" rel="stylesheet">
<style>
  :root {
    --backdrop: #222223;
    --card: #fbfbfb;
    --ink: #1c1c1e;
    --muted: #4a4a4e;
    --navy: #2e3f94;
    --soft-blue: #6f86c8;
  }
  * { margin: 0; padding: 0; box-sizing: border-box; }
  html, body { width: 1200px; height: 900px; overflow: hidden; }
  body {
    background: var(--backdrop);
    display: flex;
    flex-direction: column;
    align-items: center;
    justify-content: center;
    gap: 40px;
  }
  .card {
    position: relative;
    width: 700px;
    height: 400px;
    background: var(--card);
    box-shadow: 0 8px 24px rgba(0,0,0,0.45);
  }
  .brand {
    display: flex;
    flex-direction: column;
    align-items: center;
    font-family: 'Montserrat', sans-serif;
    color: var(--ink);
  }
  .brand-mark {
    width: 22px; height: 22px;
    border-radius: 50%;
    background: var(--navy);
    margin-bottom: 18px;
  }
  .brand-name { font-weight: 700; letter-spacing: 1px; }
  .brand-tag {
    font-weight: 300;
    text-transform: uppercase;
    color: var(--muted);
  }

  /* Front */
  .card-front { display: flex; align-items: center; justify-content: center; }
  .card-front .brand-name { font-size: 36px; }
  .card-front .brand-tag { font-size: 14px; letter-spacing: 14px; margin-top: 6px; padding-left: 14px; }

  /* Back */
  .card-back .brand { position: absolute; top: 62px; left: 0; right: 0; }
  .card-back .brand-name { font-size: 24px; }
  .card-back .brand-tag { font-size: 11px; letter-spacing: 11px; margin-top: 4px; padding-left: 11px; }

  .person {
    position: absolute;
    right: 56px; top: 160px;
    text-align: right;
    font-family: 'Lato', sans-serif;
  }
  .person-name { color: var(--navy); font-size: 21px; font-weight: 400; }
  .person-role { color: var(--muted); font-size: 14px; margin-top: 2px; }

  .divider {
    position: absolute;
    left: 70px; right: 56px; top: 225px;
    height: 2px;
    background: linear-gradient(90deg, var(--soft-blue), var(--navy));
  }

  .contact-list {
    position: absolute;
    left: 70px; top: 252px;
    list-style: none;
    font-family: 'Lato', sans-serif;
    font-size: 15px;
    color: var(--ink);
  }
  .contact-list li { display: flex; align-items: center; gap: 12px; margin-bottom: 12px; }
  .contact-list svg { width: 16px; height: 16px; fill: var(--navy); flex: none; }

  .address {
    position: absolute;
    right: 56px; top: 252px;
    text-align: right;
    font-family: 'Lato', sans-serif;
    font-size: 15px;
    line-height: 1.5;
    color: var(--ink);
  }
</style>
</head>
<body>

  <section class="card card-front">
    <div class="brand">
      <span class="brand-mark"></span>
      <span class="brand-name">Harlow &amp; Partners</span>
      <span class="brand-tag">Lawyers</span>
    </div>
  </section>

  <section class="card card-back">
    <div class="brand">
      <span class="brand-name">Harlow &amp; Partners</span>
      <span class="brand-tag">Lawyers</span>
    </div>

    <div class="person">
      <div class="person-name">Maren Ellis</div>
      <div class="person-role">Practise Manager</div>
    </div>

    <div class="divider"></div>

    <ul class="contact-list">
      <li>
        <svg viewBox="0 0 24 24" aria-hidden="true"><path d="M6.6 10.8a15.1 15.1 0 0 0 6.6 6.6l2.2-2.2a1 1 0 0 1 1-.25 11.4 11.4 0 0 0 3.6.57 1 1 0 0 1 1 1V20a1 1 0 0 1-1 1A17 17 0 0 1 3 4a1 1 0 0 1 1-1h3.5a1 1 0 0 1 1 1c0 1.25.2 2.45.57 3.57a1 1 0 0 1-.25 1z"/></svg>
        (02) 5550 1847
      </li>
      <li>
        <svg viewBox="0 0 24 24" aria-hidden="true"><path d="M3 5h18a1 1 0 0 1 1 1v12a1 1 0 0 1-1 1H3a1 1 0 0 1-1-1V6a1 1 0 0 1 1-1zm1 2.3V17h16V7.3l-8 5.2z M4.6 7 12 11.8 19.4 7z"/></svg>
        maren.ellis@harlowandpartners.com.au
      </li>
      <li>
        <svg viewBox="0 0 24 24" aria-hidden="true"><path d="M12 2a10 10 0 1 0 0 20 10 10 0 0 0 0-20zm0 2c.9 0 2.2 1.9 2.8 5H9.2C9.8 5.9 11.1 4 12 4zM4.3 11h2.8a18 18 0 0 1 .2-2H5a8 8 0 0 0-.7 2zm0 2a8 8 0 0 0 .7 2h2.3a18 18 0 0 1-.2-2zm4.8 0h5.8a16 16 0 0 1-.2 2H9.3a16 16 0 0 1-.2-2zm0-2a16 16 0 0 1 .2-2h5.4a16 16 0 0 1 .2 2zm7.8 0a18 18 0 0 0-.2-2H19a8 8 0 0 1 .7 2zm0 2h2.8a8 8 0 0 1-.7 2h-2.3a18 18 0 0 0 .2-2zM12 20c-.9 0-2.2-1.9-2.8-3h5.6c-.6 1.1-1.9 3-2.8 3z"/></svg>
        www.harlowandpartners.com.au
      </li>
    </ul>

    <address class="address" style="font-style: normal;">
      Suite 4, 12 Coral Lane<br>
      SEASIDE NSW 2099
    </address>
  </section>

</body>
</html>
```